Cryptocurrency Advisor Business Card

Dravelin Consulting Services is my company, which advises many projects in the ICO/Cryptocurrency industry. I'd like to get a sleek, preferably matte black or matte dark blue finish, business card with the company name (and simple logo w/ crypto feel) on one side and while the other side I'd like a small twitter and telegram logo together maybe separated by a / as it's the same, then an email and a phone logo so I can insert those specifics there (no address). Can have name then CEO section too. At the bottom of that section, find a place for more of a job description: ICO Advisor, World Champion Gamer, Esports Award Winner, Quorvane Expert. You can possibly design a simple logo or use something with a crypto twist or background, but nothing too complex. Rounded edges for printing not square.
Updates

Had personal issues taking a few days away from me being able to provide feedback and check designs, etc. Will be more active now finalizing design just needed few days from issue but all is sorted.

Target Market(s)

Cryptocurrency industry

Industry/Entity Type

Management Consulting

Contact Information for Business Card

Font styles to use
Sans Serif

Colors
5c5c5c
474747
757575
9d9d9d
aaaaaa
333333
0355a3

Requirements
Must have
• Refer to Details/Description
Nice to have
Should not have
• Address section

```html
<!DOCTYPE html>
<html lang="en">
<head>
<meta charset="utf-8">
<title>Dravelin Consulting Services – Business Card</title>
<link rel="stylesheet" href="https://fonts.googleapis.com/css2?family=Montserrat:wght@600&family=Oswald:wght@500&family=Work+Sans:wght@400;500&display=swap">
<style>
  :root {
    --backdrop: #333333;
    --card: #1f1f20;
    --card-edge: #262627;
    --brand-blue: #0355a3;
    --text-light: #f2f2f2;
    --text-muted: #aaaaaa;
    --rule: #e6e6e6;
  }
  * { box-sizing: border-box; margin: 0; padding: 0; }
  html, body {
    width: 1200px; height: 900px; overflow: hidden;
    background: var(--backdrop);
  }
  .canvas {
    position: relative; width: 1200px; height: 900px;
    display: flex; flex-direction: column; align-items: center;
    justify-content: center; gap: 30px;
  }
  .card {
    position: relative; width: 700px; height: 400px;
    background: linear-gradient(135deg, var(--card-edge), var(--card));
    border-radius: 16px; overflow: hidden;
    box-shadow: 0 10px 30px rgba(0,0,0,.45);
  }
  .card::after {
    content: ""; position: absolute; left: 0; right: 0; bottom: 0;
    height: 7px; background: var(--brand-blue);
  }

  /* Front */
  .brand {
    position: absolute; top: 110px; left: 0; right: 0;
    display: flex; align-items: center; justify-content: center; gap: 26px;
  }
  .brand-dot {
    width: 96px; height: 96px; border-radius: 50%;
    background: var(--brand-blue); flex: none;
  }
  .brand-name {
    font-family: "Montserrat", sans-serif; font-weight: 600;
    color: var(--brand-blue); line-height: 1.05;
  }
  .brand-name .primary { display: block; font-size: 48px; letter-spacing: 1px; }
  .brand-name .secondary { display: block; font-size: 24px; letter-spacing: 1px; }
  .roles {
    position: absolute; bottom: 42px; left: 0; right: 0;
    text-align: center; font-family: "Work Sans", sans-serif;
    font-size: 17px; line-height: 1.45; color: var(--text-light);
  }
  .roles .sep { color: var(--brand-blue); padding: 0 4px; }

  /* Back */
  .identity {
    position: absolute; top: 130px; left: 90px; width: 250px; text-align: right;
  }
  .person-name {
    font-family: "Oswald", sans-serif; font-weight: 500; font-size: 40px;
    letter-spacing: .5px; color: var(--brand-blue); line-height: 1.1;
    white-space: nowrap;
  }
  .person-title {
    font-family: "Work Sans", sans-serif; font-size: 17px;
    color: var(--text-light); letter-spacing: 1px;
  }
  .divider {
    position: absolute; top: 130px; left: 370px; width: 2px; height: 82px;
    background: var(--rule);
  }
  .contacts {
    position: absolute; top: 132px; left: 395px; list-style: none;
    font-family: "Work Sans", sans-serif; font-size: 18px;
    color: var(--text-light); line-height: 26px;
  }
  .contacts li { display: flex; align-items: center; gap: 12px; }
  .contacts svg { width: 13px; height: 13px; flex: none; }
  .social {
    position: absolute; bottom: 58px; left: 150px;
    display: flex; gap: 34px; font-family: "Work Sans", sans-serif;
    font-size: 19px; color: var(--text-light);
  }
  .social span { display: flex; align-items: center; gap: 10px; }
  .social .mark {
    width: 14px; height: 14px; border-radius: 50%; background: var(--brand-blue);
  }
</style>
</head>
<body>
<main class="canvas">
  <section class="card card-front" aria-label="Card front">
    <div class="brand">
      <span class="brand-dot"></span>
      <div class="brand-name">
        <span class="primary">Dravelin</span>
        <span class="secondary">Consulting Services</span>
      </div>
    </div>
    <p class="roles">
      ICO Advisor<span class="sep">-</span>World Champion Gamer<br>
      Esports Award Winner<span class="sep">-</span>Quorvane Expert.
    </p>
  </section>

  <section class="card card-back" aria-label="Card back">
    <div class="identity">
      <h1 class="person-name">ELIAS DRAVELIN</h1>
      <p class="person-title">CEO</p>
    </div>
    <div class="divider"></div>
    <ul class="contacts">
      <li>
        <svg viewBox="0 0 24 24" aria-hidden="true"><path fill="#0355a3" d="M6.6 10.8a15 15 0 0 0 6.6 6.6l2.2-2.2c.3-.3.7-.4 1-.2 1.1.4 2.3.6 3.6.6.6 0 1 .4 1 1V20c0 .6-.4 1-1 1A17 17 0 0 1 3 4c0-.6.4-1 1-1h3.5c.6 0 1 .4 1 1 0 1.3.2 2.5.6 3.6.1.3 0 .7-.2 1z"/></svg>
        +330 5812-4467
      </li>
      <li>
        <svg viewBox="0 0 24 24" aria-hidden="true"><rect x="2" y="5" width="20" height="14" rx="2" fill="none" stroke="#0355a3" stroke-width="2"/><path d="M3 6l9 7 9-7" fill="none" stroke="#0355a3" stroke-width="2"/></svg>
        dravelin@consulting.com
      </li>
      <li>
        <svg viewBox="0 0 24 24" aria-hidden="true"><circle cx="12" cy="12" r="9" fill="none" stroke="#0355a3" stroke-width="2"/><path d="M3 12h18M12 3c3 3 3 15 0 18M12 3c-3 3-3 15 0 18" fill="none" stroke="#0355a3" stroke-width="1.6"/></svg>
        dravelinconsulting.com
      </li>
    </ul>
    <div class="social">
      <span><i class="mark"></i>@dravelinconsulting</span>
      <span><i class="mark"></i>987 654 321</span>
    </div>
  </section>
</main>
</body>
</html>
```